New corporate Powerpoint template *

Hi,
We would like to have one new corporate Powerpoint template which can be used for various presentations (Sales, Investors, Marketing, Engineers, HR, Corporate presentations…) Please note that this template will be used for both internal and external presentations.
Please take a look at our website to get a feel for our branding.
https://www.vemtra-microdevices.example/

Some visual elements to include:

• The theme needs to be relevant to our industry i.e. Semiconductor theme (circuit board/chip graphic elements)
• Simple uses of color, lifestyle images, moving away from Geometric patterns and colorful wave
• Style should be modern, clean and gender neutral
• Use Vemtra blue as more of an accent color - Avoid the overuse of blue (seems a little too bright sometimes)
• Vemtra logo to appear on every page

Necessary slides to include:
• Cover Slide
• Agenda Slide
• Divider / Title Slide
• Content Slide
• White Slide
• Comparison slide (two, three, four)
• Table slide with the ability to add rows/columns
• Timeline/roadmap slide
• End Slide

Target Market(s)

Semiconductor industry

Font styles to use
Other font styles liked:
• Arial or Rockwell

Colors
33a6d7

Requirements
Must have
• • The theme needs to be relevant to our industry i.e. Semiconductor theme (circuit board/chip graphic elements)
• • Simple uses of color, lifestyle images
• • Style should be modern, clean and gender neutral
• • Use Vemtra blue as more of an accent color
• • Vemtra logo to appear on every page
• Necessary slides to include:
• • Cover Slide
• • Agenda Slide
• • Divider / Title Slide
• • Content Slide
• • White Slide
• • Comparison slide (two, three, four)
• • Table slide with the ability to add rows/columns
• • Timeline/roadmap slide
• • End Slide
Should not have
• - Avoid the overuse of blue (seems a little too bright sometimes)
• - Do not use any kind of wave as a graphic

```html
<!DOCTYPE html>
<html lang="en">
<head>
<meta charset="utf-8">
<title>Vemtra Corporate Template</title>
<link href="https://fonts.googleapis.com/css2?family=Arimo:wght@400;700&display=swap" rel="stylesheet">
<style>
:root{
  --board:#1f4b7c;
  --accent:#33a6d7;
  --ink:#555b61;
  --muted:#8a9096;
  --title:#6b7075;
  --panel:#eeeff0;
  --dark:#5f6367;
  --white:#ffffff;
}
*{box-sizing:border-box;margin:0;padding:0}
html,body{width:1200px;height:2723px;overflow:hidden}
body{background:var(--board);font-family:"Arimo",Arial,sans-serif;color:var(--ink)}
.deck{display:grid;grid-template-columns:552px 552px;column-gap:28px;row-gap:26px;padding:27px 33px 0}
.slide{position:relative;width:552px;height:310px;background:var(--white);overflow:hidden}
.slide-title{position:absolute;left:14px;top:7px;font-size:19px;color:var(--title);font-weight:400}
.slide-title small{font-size:11px}
.brand{position:absolute;right:12px;top:8px;display:flex;align-items:center;gap:4px;font-size:18px;font-weight:700;color:var(--accent)}
.brand .dot{width:11px;height:11px;border-radius:50%;background:var(--accent)}
.mark{position:absolute;left:14px;bottom:14px;width:34px;height:34px;border-radius:50%;background:var(--accent)}
.photo{position:absolute}
.lorem{font-size:8.5px;line-height:1.32;color:var(--muted)}

/* cover */
.cover .photo{inset:0;background:linear-gradient(120deg,#f4f6f8 0%,#dfe4e8 45%,#eef1f3 70%,#c9d3da 100%)}
.cover .brand-lg{position:absolute;left:0;right:0;top:22px;display:flex;justify-content:center;align-items:center;gap:7px;font-size:36px;font-weight:700;color:var(--accent)}
.cover .brand-lg .dot{width:22px;height:22px;border-radius:50%;background:var(--accent)}
.cover .title-box{position:absolute;left:91px;top:104px;width:375px;height:106px;background:rgba(255,255,255,.9);display:flex;align-items:center;justify-content:center;text-align:center;font-size:31px;line-height:1.18;color:var(--accent)}

/* agenda */
.agenda .intro{position:absolute;left:40px;top:72px;width:184px;text-align:right;font-size:8.8px;line-height:1.3;color:var(--ink)}
.agenda .rule{position:absolute;left:240px;top:70px;width:1px;height:200px;background:#d9dcdf}
.agenda .item{position:absolute;left:254px;display:flex;gap:10px;width:280px}
.agenda .num{flex:none;width:22px;height:22px;border-radius:50%;border:1.5px solid var(--accent);color:var(--accent);font-size:11px;display:flex;align-items:center;justify-content:center}
.agenda .item p{font-size:8.8px;line-height:1.3;color:var(--ink)}

/* section */
.section .photo{inset:0;background:linear-gradient(100deg,#eef0f2 0%,#d8dde1 30%,#e9ecee 55%,#cfe6f2 75%,#2f9fd4 100%)}
.section .label{position:absolute;left:230px;top:91px;width:284px;height:118px;background:rgba(110,116,122,.82);color:var(--white);font-size:28px;display:flex;align-items:center;padding-left:18px}

/* about */
.about .photo{left:0;right:0;top:40px;height:241px;background:linear-gradient(90deg,#c9ced2,#aeb5ba 40%,#9aa1a6 100%)}
.about .panel{position:absolute;left:182px;top:51px;width:370px;height:212px;background:rgba(85,90,95,.92);padding:14px 16px}
.about h3{font-size:13.5px;font-weight:400;color:var(--accent);margin-bottom:7px}
.about p{font-size:10.4px;line-height:1.32;color:var(--white)}

/* content */
.content .lead{position:absolute;left:40px;top:70px;font-size:12.5px;color:var(--accent)}
.content .body{position:absolute;left:40px;top:92px;width:440px}
.content .body p{font-size:8.8px;line-height:1.32;color:var(--muted);margin-bottom:7px}

/* comparison */
.card{position:absolute;background:var(--panel)}
.card h4{background:var(--accent);color:var(--white);font-size:11px;font-weight:700;padding:4px 7px;margin-bottom:6px}
.card p{padding:0 7px;font-size:8.3px;line-height:1.32;color:var(--muted)}

/* table */
.grid-table{position:absolute;left:76px;top:64px;width:400px;border-collapse:collapse;font-size:9px}
.grid-table th{background:var(--dark);color:var(--white);font-weight:700;text-align:left;padding:6px 8px}
.grid-table td{padding:7px 8px;color:var(--muted);border-bottom:1px solid #e2e4e6}
.grid-table tr:last-child td{border-bottom:1.5px solid var(--accent)}
.table .note{position:absolute;left:76px;top:246px;width:400px;font-size:9px;line-height:1.32;color:var(--muted)}

/* timeline */
.timeline .axis{position:absolute;left:0;top:0}
.event{position:absolute;width:72px;transform:translateX(-50%);text-align:center}
.event .tag{background:var(--panel);font-size:8px;line-height:1.25;color:var(--ink);padding:5px 4px}
.event .year{font-size:12.5px;color:var(--ink);margin:3px 0}
.event.up{bottom:170px}
.event.down{top:170px}

/* products */
.products .photo{inset:0;background:linear-gradient(110deg,#ffffff 0%,#f3f5f6 55%,#e4e8eb 100%)}
.products .lead{position:absolute;left:0;right:0;top:26px;text-align:center;font-size:12px;color:var(--accent)}
.products .intro{position:absolute;left:48px;top:42px;width:470px;font-size:7.6px;line-height:1.3;color:var(--ink)}
.products .line{position:absolute;display:grid;grid-template-columns:repeat(4,108px);column-gap:12px;left:48px}
.prod .head{display:flex;align-items:center;gap:4px;font-size:9px;color:var(--ink);margin-bottom:3px}
.prod .ic{width:12px;height:12px;border-radius:50%;background:var(--accent);flex:none}
.prod p{font-size:6.6px;line-height:1.28;color:var(--ink)}

/* career */
.role{position:absolute;top:60px;width:112px;transform:translateX(-50%);text-align:center}
.role h5{font-size:9px;font-weight:700;color:var(--ink);margin:6px 0 12px}
.role p{font-size:7.2px;line-height:1.3;color:var(--ink);text-align:left}

/* contact */
.contact .brand-lg{position:absolute;left:218px;top:68px;display:flex;align-items:center;gap:6px;font-size:32px;font-weight:700;color:var(--accent)}
.contact .brand-lg .dot{width:18px;height:18px;border-radius:50%;background:var(--accent)}
.contact .row{position:absolute;left:210px;display:flex;gap:12px;align-items:flex-start;font-size:9.5px;line-height:1.3;color:var(--ink)}

/* thanks */
.thanks .photo{inset:0;background:linear-gradient(135deg,#eceeef 0%,#d3d7da 50%,#c4c9cd 100%)}
.thanks .word{position:absolute;left:0;right:0;top:92px;text-align:center;font-size:58px;font-weight:700;letter-spacing:2px;color:#f4f5f6;-webkit-text-stroke:1px #b8bec3}
.thanks .big-mark{position:absolute;left:246px;top:190px;width:60px;height:60px;border-radius:50%;background:var(--accent)}
</style>
</head>
<body>
<main class="deck">

  <section class="slide cover">
    <div class="photo" role="img" aria-label="Soft, light lifestyle photograph in grey and pale blue tones"></div>
    <div class="brand-lg"><span class="dot"></span>vemtra</div>
    <div class="title-box">Presentation Title<br>Here</div>
    <div class="mark"></div>
  </section>

  <section class="slide agenda">
    <h2 class="slide-title">Agenda Layout</h2>
    <p class="intro">Lorem ipsum dolor sit amet, consectetur adipiscing elit. Integer nec odio. Praesent libero. Sed cursus ante dapibus diam. Sed nisi. Nulla quis sem at nibh elementum imperdiet. Duis sagittis ipsum. Praesent mauris. Fusce nec tellus sed augue semper porta. Mauris massa. Vestibulum lacinia arcu eget nulla.</p>
    <div class="rule"></div>
    <div class="item" style="top:80px"><span class="num">1</span><p>Lorem ipsum dolor sit amet, consectetur adipiscing elit. Integer nec odio. Praesent libero. Sed cursus ante dapibus diam</p></div>
    <div class="item" style="top:138px"><span class="num">2</span><p>Lorem ipsum dolor sit amet, consectetur adipiscing elit. Integer nec odio. Praesent libero. Sed cursus ante dapibus diam</p></div>
    <div class="item" style="top:195px"><span class="num">3</span><p>Lorem ipsum dolor sit amet, consectetur adipiscing elit. Integer nec odio. Praesent libero. Sed cursus ante dapibus diam</p></div>
    <div class="item" style="top:252px"><span class="num">4</span><p>Lorem ipsum dolor sit amet, consectetur adipiscing elit. Integer nec odio. Praesent libero. Sed cursus ante dapibus diam</p></div>
    <div class="mark"></div>
  </section>

  <section class="slide section">
    <div class="photo" role="img" aria-label="Lifestyle photograph of a business professional on the phone, fading into an accent blue band"></div>
    <div class="label">Section Break</div>
    <div class="mark"></div>
  </section>

  <section class="slide about">
    <h2 class="slide-title">About Us</h2>
    <div class="brand"><span class="dot"></span>vemtra</div>
    <div class="photo" role="img" aria-label="Muted grey photograph of a modern workplace"></div>
    <div class="panel">
      <h3>Innovation is at the core of our business</h3>
      <p>Our top talent and technology, paired with an innovative product-development philosophy and sustained engineering investment, allows us to provide the highest performance power saving solutions to its customers, particularly for smartphones, power adapters, solid state lighting and emerging IoT applications. Leveraging advanced system-level knowhow and a deep portfolio of intellectual property with advanced mixed signal innovation, enables Vemtra to consistently deliver extraordinary value to our customers.</p>
    </div>
  </section>

  <section class="slide content">
    <h2 class="slide-title">Content Slide</h2>
    <div class="brand"><span class="dot"></span>vemtra</div>
    <h3 class="lead">Building a vibrant and innovative mixed-signal business</h3>
    <div class="body">
      <p>Vemtra brings decades of experience to the rapid development of ICs while providing flexible and dynamic support, world-class innovation and the assurance of dealing with an established business partner. We continue to lead through innovation and diversification as a socially responsible employer pursuing many programs to benefit the employees, community, stakeholders and the environment we operate in.</p>
      <p>Our employees are engaged, motivated and highly skilled. Our talented employees drive our innovation and success, focusing on power management, power conversion and other power efficient connectivity and lighting solutions for mobile and consumer applications. Help us continue our impressive growth into exciting new products and markets.</p>
      <p>Our performance reflects Vemtra's focused delivery on competitive and differentiated products in high growth consumer electronics markets through the continued innovation, hard work and dedication of all our employees.</p>
    </div>
  </section>

  <section class="slide white">
    <h2 class="slide-title">White Slide</h2>
    <div class="brand"><span class="dot"></span>vemtra</div>
  </section>

  <section class="slide compare-two">
    <h2 class="slide-title">Comparison Slide</h2>
    <div class="brand"><span class="dot"></span>vemtra</div>
    <div class="card" style="left:82px;top:64px;width:186px;height:200px"><h4>Content A</h4><p>Lorem ipsum dolor sit amet, consectetur adipiscing elit. Integer nec odio. Praesent libero. Sed cursus ante dapibus diam. Sed nisi. Nulla quis sem at nibh elementum imperdiet. Duis sagittis ipsum. Praesent mauris. Fusce nec tellus sed augue semper porta. Mauris massa. Vestibulum lacinia arcu eget nulla. Class aptent taciti sociosqu ad litora torquent per conubia nostra, per inceptos himenaeos. Curabitur sodales ligula in libero. Sed dignissim lacinia nunc. Curabitur tortor. Pellentesque nibh. Aenean quam. In scelerisque sem at dolor. Maecenas mattis. Sed convallis tristique sem</p></div>
    <div class="card" style="left:289px;top:64px;width:186px;height:200px"><h4>Content B</h4><p>Lorem ipsum dolor sit amet, consectetur adipiscing elit. Integer nec odio. Praesent libero. Sed cursus ante dapibus diam. Sed nisi. Nulla quis sem at nibh elementum imperdiet. Duis sagittis ipsum. Praesent mauris. Fusce nec tellus sed augue semper porta. Mauris massa. Vestibulum lacinia arcu eget nulla. Class aptent taciti sociosqu ad litora torquent per conubia nostra, per inceptos himenaeos. Curabitur sodales ligula in libero. Sed dignissim lacinia nunc. Curabitur tortor. Pellentesque nibh. Aenean quam. In scelerisque sem at dolor. Maecenas mattis. Sed convallis tristique sem</p></div>
  </section>

  <section class="slide compare-three">
    <h2 class="slide-title">Comparison Slide</h2>
    <div class="brand"><span class="dot"></span>vemtra</div>
    <div class="card" style="left:36px;top:72px;width:150px;height:190px"><h4>Content A</h4><p>Lorem ipsum dolor sit amet, consectetur adipiscing elit. Integer nec odio. Praesent libero. Sed cursus ante dapibus diam. Sed nisi. Nulla quis sem at nibh elementum imperdiet. Duis sagittis ipsum. Praesent mauris. Fusce nec tellus sed augue semper porta. Mauris massa. Vestibulum lacinia arcu eget nulla. Class aptent taciti sociosqu ad litora torquent per conubia nostra, per inceptos himenaeos. Curabitur sodales ligula in libero. Sed dignissim lacinia nunc.</p></div>
    <div class="card" style="left:202px;top:72px;width:150px;height:190px"><h4>Content B</h4><p>Lorem ipsum dolor sit amet, consectetur adipiscing elit. Integer nec odio. Praesent libero. Sed cursus ante dapibus diam. Sed nisi. Nulla quis sem at nibh elementum imperdiet. Duis sagittis ipsum. Praesent mauris. Fusce nec tellus sed augue semper porta. Mauris massa. Vestibulum lacinia arcu eget nulla. Class aptent taciti sociosqu ad litora torquent per conubia nostra, per inceptos himenaeos. Curabitur sodales ligula in libero. Sed dignissim lacinia nunc.</p></div>
    <div class="card" style="left:368px;top:72px;width:150px;height:190px"><h4>Content C</h4><p>Lorem ipsum dolor sit amet, consectetur adipiscing elit. Integer nec odio. Praesent libero. Sed cursus ante dapibus diam. Sed nisi. Nulla quis sem at nibh elementum imperdiet. Duis sagittis ipsum. Praesent mauris. Fusce nec tellus sed augue semper porta. Mauris massa. Vestibulum lacinia arcu eget nulla. Class aptent taciti sociosqu ad litora torquent per conubia nostra, per inceptos himenaeos. Curabitur sodales ligula in libero. Sed dignissim lacinia nunc.</p></div>
  </section>

  <section class="slide compare-four">
    <h2 class="slide-title">Comparison Slide</h2>
    <div class="brand"><span class="dot"></span>vemtra</div>
    <div class="card" style="left:92px;top:58px;width:172px;height:104px"><h4>Content A</h4><p>Lorem ipsum dolor sit amet, consectetur adipiscing elit. Integer nec odio. Praesent libero. Sed cursus ante dapibus diam. Sed nisi. Nulla quis sem at nibh elementum imperdiet. Duis sagittis ipsum. Praesent mauris.</p></div>
    <div class="card" style="left:300px;top:58px;width:172px;height:104px"><h4>Content B</h4><p>Lorem ipsum dolor sit amet, consectetur adipiscing elit. Integer nec odio. Praesent libero. Sed cursus ante dapibus diam. Sed nisi. Nulla quis sem at nibh elementum imperdiet. Duis sagittis ipsum. Praesent mauris.</p></div>
    <div class="card" style="left:92px;top:178px;width:172px;height:104px"><h4>Content C</h4><p>Lorem ipsum dolor sit amet, consectetur adipiscing elit. Integer nec odio. Praesent libero. Sed cursus ante dapibus diam. Sed nisi. Nulla quis sem at nibh elementum imperdiet. Duis sagittis ipsum. Praesent mauris.</p></div>
    <div class="card" style="left:300px;top:178px;width:172px;height:104px"><h4>Content D</h4><p>Lorem ipsum dolor sit amet, consectetur adipiscing elit. Integer nec odio. Praesent libero. Sed cursus ante dapibus diam. Sed nisi. Nulla quis sem at nibh elementum imperdiet. Duis sagittis ipsum. Praesent mauris.</p></div>
  </section>

  <section class="slide table">
    <h2 class="slide-title">Table Slide</h2>
    <div class="brand"><span class="dot"></span>vemtra</div>
    <table class="grid-table">
      <thead><tr><th>Title A</th><th>Title B</th><th>Title C</th><th>Title D</th><th>Title E</th><th>Title F</th></tr></thead>
      <tbody>
        <tr><td>Text Here</td><td>Text Here</td><td>Text Here</td><td>Text Here</td><td>Text Here</td><td>Text Here</td></tr>
        <tr><td>Content</td><td>Content</td><td>Content</td><td>Content</td><td>Content</td><td>Content</td></tr>
        <tr><td>Text Here</td><td>Text Here</td><td>Text Here</td><td>Text Here</td><td>Text Here</td><td>Text Here</td></tr>
        <tr><td>Content</td><td>Content</td><td>Content</td><td>Content</td><td>Content</td><td>Content</td></tr>
        <tr><td>Text Here</td><td>Text Here</td><td>Text Here</td><td>Text Here</td><td>Text Here</td><td>Text Here</td></tr>
      </tbody>
    </table>
    <p class="note">This text can be replaced with your own text. This text can be replaced with your own text. This text can be replaced with your own text. This text can be replaced with your own text. This text can be replaced with your own text</p>
  </section>

  <section class="slide timeline">
    <h2 class="slide-title">Timeline Slide</h2>
    <div class="brand"><span class="dot"></span>vemtra</div>
    <svg class="axis" width="552" height="310" viewBox="0 0 552 310" aria-hidden="true">
      <line x1="73" y1="158" x2="512" y2="158" stroke="#4a4f54" stroke-width="2"/>
      <polygon points="512,152 522,158 512,164" fill="#4a4f54"/>
      <g fill="#1f4b7c" stroke="#ffffff" stroke-width="2">
        <circle cx="73" cy="158" r="6"/><circle cx="155" cy="158" r="6"/><circle cx="237" cy="158" r="6"/>
        <circle cx="319" cy="158" r="6"/><circle cx="401" cy="158" r="6"/><circle cx="483" cy="158" r="6"/>
      </g>
      <g stroke="#c9cdd0" stroke-width="1">
        <line x1="73" y1="140" x2="73" y2="150"/><line x1="237" y1="140" x2="237" y2="150"/><line x1="401" y1="140" x2="401" y2="150"/>
        <line x1="155" y1="166" x2="155" y2="176"/><line x1="319" y1="166" x2="319" y2="176"/><line x1="483" y1="166" x2="483" y2="176"/>
      </g>
    </svg>
    <div class="event up" style="left:73px"><div class="year">1981</div><div class="tag">Vemtra originates from Korvan</div></div>
    <div class="event up" style="left:237px"><div class="year">1990</div><div class="tag">Vemtra Semiconductor formed</div></div>
    <div class="event up" style="left:401px"><div class="year">1998</div><div class="tag">LBO from Halbern-Ostrand</div></div>
    <div class="event down" style="left:155px"><div class="tag">Korvan Europe founded</div><div class="year">1986</div></div>
    <div class="event down" style="left:319px"><div class="tag">Becomes part of Halbern-Ostrand</div><div class="year">1992</div></div>
    <div class="event down" style="left:483px"><div class="tag">IPO Frankfurt</div><div class="year">1999</div></div>
  </section>

  <section class="slide timeline">
    <h2 class="slide-title">Timeline Slide <small>(continued)</small></h2>
    <div class="brand"><span class="dot"></span>vemtra</div>
    <svg class="axis" width="552" height="310" viewBox="0 0 552 310" aria-hidden="true">
      <line x1="50" y1="158" x2="522" y2="158" stroke="#4a4f54" stroke-width="2"/>
      <g fill="#1f4b7c" stroke="#ffffff" stroke-width="2">
        <circle cx="73" cy="158" r="6"/><circle cx="134" cy="158" r="6"/><circle cx="195" cy="158" r="6"/><circle cx="256" cy="158" r="6"/>
        <circle cx="317" cy="158" r="6"/><circle cx="378" cy="158" r="6"/><circle cx="439" cy="158" r="6"/><circle cx="500" cy="158" r="6"/>
      </g>
      <g stroke="#c9cdd0" stroke-width="1">
        <line x1="73" y1="140" x2="73" y2="150"/><line x1="195" y1="140" x2="195" y2="150"/><line x1="378" y1="140" x2="378" y2="150"/><line x1="500" y1="140" x2="500" y2="150"/>
        <line x1="134" y1="166" x2="134" y2="176"/><line x1="256" y1="166" x2="256" y2="176"/><line x1="439" y1="166" x2="439" y2="176"/>
      </g>
    </svg>
    <div class="event up" style="left:73px"><div class="year">2005</div><div class="tag">New management team</div></div>
    <div class="event up" style="left:195px"><div class="year">2008</div><div class="tag">Return to full year profitability</div></div>
    <div class="event up" style="left:378px"><div class="year">2012</div><div class="tag">Vemtra pioneers integration of Kestrel processor</div></div>
    <div class="event up" style="left:500px"><div class="year">2015</div><div class="tag">Vemtra originates from Korvan</div></div>
    <div class="event down" style="left:134px"><div class="tag">Launch of new products optimized for portable devices</div><div class="year">2006</div></div>
    <div class="event down" style="left:256px"><div class="tag">Acquisition of Quvix</div><div class="year">2011</div></div>
    <div class="event down" style="left:439px"><div class="tag">Vemtra acquires Zelto</div><div class="year">2013</div></div>
  </section>

  <section class="slide products">
    <div class="photo" role="img" aria-label="Faint background photograph of a bright office"></div>
    <h2 class="slide-title">Products</h2>
    <div class="brand"><span class="dot"></span>vemtra</div>
    <h3 class="lead">Personal + Portable + Connected</h3>
    <p class="intro">Our power saving solutions are integral to some of today's leading mobile devices and the enabling element for increasing performance and productivity on the go. From making smartphones more power efficient and shortening charging times, enabling home appliances to be controlled from anywhere, to connecting the next generation of wearable devices. Vemtra's decades of experience and world-class innovation help manufacturers get to what's next.</p>
    <div class="line" style="top:100px">
      <div class="prod"><div class="head"><span class="ic"></span>Power Management</div><p>With its unique focus and expertise in system power management Vemtra brings great power supply domain flexibility to personal portable applications.</p></div>
      <div class="prod"><div class="head"><span class="ic"></span>Connectivity</div><p>Reliable, powerful, and easy-to-use, our wireless connectivity product family delivers outstanding performance, flexibility and improved battery life to wearables and smart home applications.</p></div>
      <div class="prod"><div class="head"><span class="ic"></span>Audio</div><p>Our high definition audio amplifiers, CODECs and audio integrated PMICs feature crystal clear audio amplification and true-ground capless headphone drivers suitable for a wide range of digital.</p></div>
      <div class="prod"><div class="head"><span class="ic"></span>Lighting</div><p>Innovative LED drivers to solve our customers' design challenges in solid state lighting and display backlighting.</p></div>
    </div>
    <div class="line" style="top:196px">
      <div class="prod"><div class="head"><span class="ic"></span>Power Conversion</div><p>Our AC/DC primary-side converters, secondary-side ICs and synchronous rectifiers solve power consumption, size and cost issues in power adapters and power supplies.</p></div>
      <div class="prod"><div class="head"><span class="ic"></span>Power Switching</div><p>Innovative design process enables highest performance integrated power switches.</p></div>
      <div class="prod"><div class="head"><span class="ic"></span>FlexMatrix</div><p>Programmable Mixed-signal Matrix.</p></div>
      <div class="prod"><div class="head"><span class="ic"></span>Timing</div><p>FlexCLK Crystal Replacement Products.</p></div>
    </div>
    <div class="mark"></div>
  </section>

  <section class="slide career">
    <h2 class="slide-title">Career</h2>
    <div class="brand"><span class="dot"></span>vemtra</div>
    <div class="role" style="left:85px">
      <svg width="48" height="58" viewBox="0 0 48 58" aria-hidden="true"><path d="M24 2a22 22 0 0 1 22 22c0 14-22 32-22 32S2 38 2 24A22 22 0 0 1 24 2z" fill="#cde9f5"/><circle cx="24" cy="24" r="16" fill="#33a6d7"/><circle cx="24" cy="20" r="5" fill="#fff"/><path d="M15 33c2-6 16-6 18 0z" fill="#fff"/></svg>
      <h5>Engineers</h5>
      <p>We excel at developing the highest performance and integrated PMICs, where feature integration and innovation is a premium. Join us as we engineer the products of the future.</p>
    </div>
    <div class="role" style="left:203px">
      <svg width="48" height="58" viewBox="0 0 48 58" aria-hidden="true"><path d="M24 2a22 22 0 0 1 22 22c0 14-22 32-22 32S2 38 2 24A22 22 0 0 1 24 2z" fill="#cde9f5"/><circle cx="24" cy="24" r="16" fill="#33a6d7"/><path d="M24 13a7 7 0 0 1 7 7c0 5-7 11-7 11s-7-6-7-11a7 7 0 0 1 7-7z" fill="#fff"/><circle cx="24" cy="20" r="2.5" fill="#33a6d7"/></svg>
      <h5>Professionals</h5>
      <p>We work with some of the best household and industry names in the world, creating market-leading applications. We are looking for dynamic individuals who strive to make a difference.</p>
    </div>
    <div class="role" style="left:330px">
      <svg width="48" height="58" viewBox="0 0 48 58" aria-hidden="true"><path d="M24 2a22 22 0 0 1 22 22c0 14-22 32-22 32S2 38 2 24A22 22 0 0 1 24 2z" fill="#cde9f5"/><circle cx="24" cy="24" r="16" fill="#33a6d7"/><polygon points="24,15 35,20 24,25 13,20" fill="#fff"/><path d="M17 23v5c3 3 11 3 14 0v-5l-7 3z" fill="#fff"/></svg>
      <h5>Graduates</h5>
      <p>Learn new skills and develop your career in a supportive and entrepreneurial environment with some of the best minds in the industry. Let's grow together.</p>
    </div>
    <div class="role" style="left:457px">
      <svg width="48" height="58" viewBox="0 0 48 58" aria-hidden="true"><path d="M24 2a22 22 0 0 1 22 22c0 14-22 32-22 32S2 38 2 24A22 22 0 0 1 24 2z" fill="#cde9f5"/><circle cx="24" cy="24" r="16" fill="#33a6d7"/><rect x="15" y="16" width="18" height="15" rx="1.5" fill="#fff"/><circle cx="24" cy="22" r="3" fill="#33a6d7"/><path d="M19 29c1-4 9-4 10 0z" fill="#33a6d7"/></svg>
      <h5>Students &amp; Internships</h5>
      <p>We offer a wide range of student sponsorships and internship positions globally. Start here.</p>
    </div>
  </section>

  <section class="slide contact">
    <h2 class="slide-title">Contact Us</h2>
    <div class="brand-lg"><span class="dot"></span>vemtra</div>
    <div class="row" style="top:136px">
      <svg width="14" height="18" viewBox="0 0 14 18" aria-hidden="true"><path d="M7 0a7 7 0 0 1 7 7c0 5-7 11-7 11S0 12 0 7a7 7 0 0 1 7-7z" fill="#555b61"/><circle cx="7" cy="7" r="2.6" fill="#fff"/></svg>
      <p>Corporate headquarters :<br>48 Harrowgate Lane<br>Northmere Park<br>Easton EN4 2QT<br>United Kingdom</p>
    </div>
    <div class="row" style="top:212px">
      <svg width="16" height="16" viewBox="0 0 16 16" aria-hidden="true"><path d="M3 1l3 3-2 2c1 2 3 4 5 5l2-2 3 3-2 3C6 15 1 10 1 3z" fill="#555b61"/></svg>
      <p>+44 (0) 1632 960418</p>
    </div>
    <div class="row" style="top:246px">
      <svg width="16" height="12" viewBox="0 0 16 12" aria-hidden="true"><rect width="16" height="12" rx="1" fill="#555b61"/><path d="M1 1l7 6 7-6" fill="none" stroke="#fff" stroke-width="1.2"/></svg>
      <p>info@vemtra.example</p>
    </div>
  </section>

  <section class="slide thanks">
    <div class="photo" role="img" aria-label="Soft grey lifestyle photograph behind the closing message"></div>
    <div class="word">THANK YOU</div>
    <div class="big-mark"></div>
  </section>

</main>
</body>
</html>
```